Tom Pelling Personal Website Yoga Teacher and Personal Fitness Trainer

Let's pick a WORDPRESS theme that can work with Video Bckground. I would like a website design to look like some of nice Squarespace themes.
I would like to have a Video background of me teaching. I can provide video. Please view my current Wordpress site: www.tompelling.example. I also have new logo. See file tpel1.png

Reason: I am guaranteeing this project because i believe designers can deliver. I am extending 5 days because the homepage image/video slider is intricate and takes a bit of time. I have provided details, images, video etc. in Dropbox. Tx

Target Market(s)

All people needing & wanting personal help (they can trust and feel safe and nurtured) for their health (wellness, nutrition, fitness, exercise). And people wanting extraordinary yoga teaching.

Industry/Entity Type

Fitness

Number of Pages Required

5+ page

Colors
9bcb3b
add136
cadf82
eaf2ce

Requirements
Must have
• Template that can use a video background
Nice to have
• Need to show good image gallery and testimonial videos

```html
<!DOCTYPE html>
<html lang="en">
<head>
<meta charset="utf-8">
<title>Tom Pelling – Yoga Teacher &amp; Personal Fitness Trainer</title>
<link href="https://fonts.googleapis.com/css2?family=Open+Sans:ital,wght@0,400;0,600;0,700;0,800;1,400;1,600;1,700&display=swap" rel="stylesheet">
<style>
:root{
  --green:#9bcb3b;
  --green-dark:#7fae25;
  --green-mid:#add136;
  --green-soft:#cadf82;
  --green-pale:#eaf2ce;
  --charcoal:#3d3d3d;
  --charcoal-2:#4a4a4a;
  --ink:#333;
  --text:#666;
  --line:#e2e2e2;
  --grey-bg:#f1f1f1;
  --white:#fff;
}
*{box-sizing:border-box;margin:0;padding:0}
html,body{width:1200px;height:2857px;overflow:hidden}
body{font-family:"Open Sans",Arial,sans-serif;color:var(--text);background:var(--white);position:relative}
.wrap{width:936px;margin:0 auto;position:relative}

/* header */
.site-header{height:156px;position:relative}
.top-tabs{position:absolute;left:613px;top:0;display:flex}
.top-tabs span{display:block;background:#5a5a5a;color:#fff;font-size:12px;font-weight:600;text-transform:uppercase;height:42px;line-height:42px;padding:0 42px;clip-path:polygon(0 0,100% 0,92% 100%,8% 100%);margin-right:-14px}
.brand{position:absolute;left:140px;top:44px;display:flex;align-items:center;gap:14px}
.brand-dot{width:54px;height:54px;border-radius:50%;background:var(--green)}
.brand-name{font-size:36px;font-weight:700;color:var(--charcoal);letter-spacing:.5px}
.contact{position:absolute;top:82px;display:flex;align-items:center;gap:10px;font-size:11px;color:#555;line-height:16px;white-space:nowrap}
.contact .ico{width:38px;height:38px;border:2px solid var(--green);border-radius:50%;display:flex;align-items:center;justify-content:center;flex:none}
.contact.email{left:728px}.contact.phone{left:944px}

/* nav */
.main-nav{height:57px;background:var(--green)}
.main-nav ul{list-style:none;display:flex;width:936px;margin:0 auto;height:57px}
.main-nav li{flex:1;text-align:center;line-height:57px;color:#fff;font-size:13px;font-weight:600;text-transform:uppercase;border-right:1px solid rgba(255,255,255,.25)}
.main-nav li.active{background:var(--charcoal)}
.main-nav li.open{background:var(--charcoal);position:relative}
.submenu{position:absolute;top:57px;left:0;width:132px;background:rgba(50,50,50,.85);text-align:left;padding:6px 0;z-index:3}
.submenu div{line-height:26px;font-size:11px;padding-left:10px}
.submenu div::before{content:"";display:inline-block;width:10px;height:3px;background:var(--green);margin-right:8px;vertical-align:middle}

/* hero */
.hero{height:539px;position:relative;background:linear-gradient(135deg,#5b7a3a 0%,#8e7a63 35%,#b48f76 55%,#4e6b30 100%)}
.hero-caption{position:absolute;left:653px;top:158px;width:414px;height:235px;background:rgba(40,40,40,.78);padding:20px 24px}
.hero-caption h1{font-size:24px;font-weight:700;color:#fff;line-height:30px;text-transform:uppercase}
.hero-caption h1 em{color:var(--green);font-style:normal}
.hero-caption p{font-size:11.5px;line-height:21px;color:#ddd;margin:10px 0 12px}
.btn{display:inline-block;background:var(--green);color:#fff;font-size:11px;font-weight:700;text-transform:uppercase;padding:0 16px;height:34px;line-height:34px;border-radius:2px}
.hero-arrow{position:absolute;top:240px;color:#fff;font-size:40px;opacity:.7}

/* features */
.features{display:flex;height:187px}
.feature{flex:1;display:flex;align-items:flex-start;color:#fff;padding-top:26px}
.feature.dark{background:var(--charcoal-2);padding-left:131px}
.feature.green{background:var(--green);padding-left:34px}
.feature .circle{width:118px;height:118px;border:3px solid #fff;border-radius:50%;flex:none;display:flex;align-items:center;justify-content:center;margin-top:10px}
.feature .body{margin-left:26px;width:300px}
.feature h3{font-size:19px;font-weight:700;line-height:27px;text-transform:uppercase}
.feature p{font-size:12px;line-height:20px;margin:8px 0 10px;opacity:.85}
.feature .more{font-size:11px;font-weight:600;text-transform:uppercase}

/* welcome */
.welcome{height:313px;border-bottom:1px solid var(--line)}
.welcome .text{position:absolute;left:0;top:42px;width:540px}
h2.title{font-size:26px;font-weight:700;color:var(--ink);text-transform:uppercase}
h2.title em{font-style:normal;color:var(--green)}
.welcome .quote{font-style:italic;font-size:13px;color:#444;margin:14px 0 10px}
.welcome p.copy{font-size:12px;line-height:23px}
.welcome .portrait{position:absolute;left:570px;top:42px;width:366px;height:212px;border:4px solid #fff;box-shadow:0 0 0 1px var(--line);background:linear-gradient(120deg,#3f6a2a,#a08068 55%,#d8d2c8)}

/* services */
.services{height:488px}
.services .head{position:absolute;top:36px;left:0}
.services .sub{font-size:12px;font-weight:600;color:#555;text-transform:uppercase;margin-top:4px}
.arrows{position:absolute;right:0;top:38px;display:flex;gap:8px}
.arrows span{width:32px;height:32px;border:1px solid #bbb;border-radius:50%;display:flex;align-items:center;justify-content:center;color:#999;font-size:14px}
.cards{position:absolute;top:107px;left:0;display:flex;gap:24px}
.card{width:296px;height:337px;background:#fff;box-shadow:0 1px 4px rgba(0,0,0,.12)}
.card .photo{height:158px}
.card h4{font-size:16px;font-weight:600;color:var(--ink);margin:22px 22px 12px}
.card p{font-size:12px;line-height:19px;margin:0 22px 16px}
.card .btn{margin-left:22px}

/* gallery */
.gallery{height:523px;background:var(--grey-bg);text-align:center}
.gallery h2.title{padding-top:38px}
.filters{display:flex;justify-content:center;gap:12px;margin-top:24px}
.filters span{height:34px;line-height:32px;border:1px solid #aaa;padding:0 18px;font-size:11px;font-weight:600;color:#555;background:#fff;text-transform:uppercase}
.filters span.on{background:var(--green);border-color:var(--green);color:#fff}
.grid{position:absolute;left:0;top:165px;width:936px;height:301px}
.grid div{position:absolute}

/* testimonials */
.testimonials{height:334px}
.testimonials .text{position:absolute;left:0;top:50px;width:540px}
.testimonials h5{font-size:15px;font-style:italic;font-weight:700;color:var(--ink);margin:18px 0 6px}
.testimonials h5::before{content:"\201C";color:var(--green);font-size:44px;font-style:normal;font-weight:800;vertical-align:-18px;margin-right:8px}
.testimonials p{font-size:11px;font-style:italic;line-height:20px}
.testimonials .who{color:var(--green);font-weight:600;font-style:italic;font-size:13px;margin-top:18px}
.testimonials .role{font-size:13px;color:#444}
.video{position:absolute;left:555px;top:58px;width:381px;height:215px;border:4px solid #fff;box-shadow:0 0 0 1px var(--line);background:linear-gradient(150deg,#e8eef2,#b9c7cf 60%,#4f8f86)}
.video .play{position:absolute;left:160px;top:80px}

/* footer */
.site-footer{height:200px;background:var(--charcoal-2);color:#fff}
.site-footer .foot-brand{position:absolute;left:0;top:40px;font-size:20px;font-weight:700;display:flex;align-items:center;gap:8px}
.foot-brand i{width:26px;height:26px;border-radius:50%;background:#777;display:block}
.socials{position:absolute;left:0;top:120px;display:flex;gap:6px}
.socials span{width:26px;height:26px;border:1px solid #aaa;border-radius:50%}
.fcol{position:absolute;top:42px;font-size:11px;line-height:23px}
.fcol h6{font-size:12px;font-weight:700;text-transform:uppercase;margin-bottom:10px}
.newsletter{position:absolute;left:725px;top:42px;width:211px;font-size:11px;line-height:18px}
.newsletter h6{font-size:12px;font-weight:700;text-transform:uppercase;margin-bottom:10px}
.subscribe{display:flex;margin-top:12px}
.subscribe span{flex:1;height:36px;background:#fff;color:#888;font-style:italic;line-height:36px;padding-left:8px}
.subscribe b{width:36px;background:var(--green);text-align:center;line-height:36px}
.copyright{height:47px;background:var(--green);color:#fff;font-size:11px;text-align:center;line-height:47px}
</style>
</head>
<body>

<header class="site-header">
  <div class="top-tabs"><span>Teacher of Yoga</span><span>Personal Fitness Trainer</span></div>
  <div class="brand"><span class="brand-dot"></span><span class="brand-name">Tom Pelling</span></div>
  <div class="contact email">
    <span class="ico"><svg width="16" height="12" viewBox="0 0 16 12"><rect x="0.5" y="0.5" width="15" height="11" fill="none" stroke="#9bcb3b"/><path d="M1 1l7 6 7-6" fill="none" stroke="#9bcb3b"/></svg></span>
    <span>Email:<br>info@tompelling.example</span>
  </div>
  <div class="contact phone">
    <span class="ico"><svg width="16" height="16" viewBox="0 0 16 16"><path d="M3 1l3 3-2 2c1 2 3 4 5 5l2-2 3 3-2 3C6 15 1 10 0 3z" fill="#9bcb3b"/></svg></span>
    <span>Phone:<br>000-000-0417</span>
  </div>
</header>

<nav class="main-nav">
  <ul>
    <li class="active">Home</li><li>About Tom</li><li>Schedule</li><li>Services ▾</li>
    <li class="open">Clients<div class="submenu"><div>Case Study</div><div>Testimonials</div></div></li>
    <li>Gallery</li><li>Contact</li>
  </ul>
</nav>

<section class="hero" role="img" aria-label="Group photo of smiling yoga students standing together outdoors among tropical plants">
  <span class="hero-arrow" style="left:14px">‹</span>
  <span class="hero-arrow" style="right:14px">›</span>
  <div class="hero-caption">
    <h1>Be the healthiest &amp;<br><em>happiest you!</em></h1>
    <p>I practice a holistic approach to nutrition, which means that I look at how all areas of your life are connected. Does stress at your job or in your relationship cause you to overeat? Does lack of sleep or low energy prevent you from exercising? As we work together,</p>
    <span class="btn">Read More</span>
  </div>
</section>

<section class="features">
  <div class="feature dark">
    <div class="circle"><svg width="60" height="60" viewBox="0 0 60 60"><path d="M30 36c-8-6-13-10-13-16a7 7 0 0 1 13-3 7 7 0 0 1 13 3c0 6-5 10-13 16z" fill="#fff"/><path d="M6 32c4 10 12 18 24 18s20-8 24-18" fill="none" stroke="#fff" stroke-width="4" stroke-linecap="round"/></svg></div>
    <div class="body"><h3>Expert guidance for<br>a healthier life</h3><p>Sed ut perspiciatis unde omnis iste natus error sit volupt atem accusantium doloremque laudantium.</p><span class="more">Read More »</span></div>
  </div>
  <div class="feature green">
    <div class="circle"><svg width="60" height="60" viewBox="0 0 60 60"><circle cx="30" cy="12" r="6" fill="#fff"/><path d="M30 20c-5 0-7 4-7 10v6h14v-6c0-6-2-10-7-10zM23 28l-10 8M37 28l10 8" stroke="#fff" stroke-width="4" fill="#fff" stroke-linecap="round"/><path d="M10 46c8-6 32-6 40 0" stroke="#fff" stroke-width="5" fill="none" stroke-linecap="round"/></svg></div>
    <div class="body"><h3>Expert leader of yoga<br>teacher training</h3><p>Sed ut perspiciatis unde omnis iste natus error sit volupt atem accusantium doloremque laudantium.</p><span class="more">Read More »</span></div>
  </div>
</section>

<section class="welcome wrap">
  <div class="text">
    <h2 class="title">Welcome to <em>Tompelling</em></h2>
    <p class="quote">" Expert Guidance for a Healthier Life"</p>
    <p class="copy">Are you at a decision point in your life, where wellness has become a priority and you are seeking additional support to reach your goals? Tom offers his unique experience to help inspire you to become healthier. He will guide you to wellness by working with you to create a custom tailored plan based on your needs and what you really want to achieve. Whether it is yoga you seek, improved nutrition, coaching, mindfulness &amp; meditation or increased fitness, Tom has the experience, skills and personality to get you there. Please take a moment to read the fabulous testimonials (and see the video testimonials) Tom has received from so many of his yoga students and fitness clients.</p>
  </div>
  <div class="portrait" role="img" aria-label="Portrait of the yoga teacher against green foliage"></div>
</section>

<section class="services wrap">
  <div class="head">
    <h2 class="title">State <em>Services</em></h2>
    <div class="sub">Yoga, wellness &amp; fitness with Tom Pelling the natural way</div>
  </div>
  <div class="arrows"><span>‹</span><span>›</span></div>
  <div class="cards">
    <div class="card">
      <div class="photo" role="img" aria-label="Yoga teacher in a wide stretching pose in a bright room" style="background:linear-gradient(160deg,#f3ede4,#d9c3a6 60%,#a8672d)"></div>
      <h4>Workshops &amp; Retreats</h4>
      <p>Sed ut perspiciatis undlorere omnis isssit olupt atem accusantiunde omniremqdptatem accusan tiunde omnireptatem accusantiun</p>
      <span class="btn">Read More</span>
    </div>
    <div class="card">
      <div class="photo" role="img" aria-label="Trainer assisting a student with a floor yoga pose" style="background:linear-gradient(160deg,#c9a886,#8a5a3a 60%,#5a3d2a)"></div>
      <h4>Personal Fitness &amp; Yoga Training</h4>
      <p>Sed ut perspiciatis undlorere omnis isssit olupt atem accusantiunde omniremqdptatem accusan tiunde omnireptatem accusantiun</p>
      <span class="btn">Read More</span>
    </div>
    <div class="card">
      <div class="photo" role="img" aria-label="Senior class stretching outdoors among palm trees" style="background:linear-gradient(160deg,#2f5a2a,#6b8a4a 55%,#d8d6c8)"></div>
      <h4>Specialty Senior Classes</h4>
      <p>Sed ut perspiciatis undlorere omnis isssit olupt atem accusantiunde omniremqdptatem accusan tiunde omnireptatem accusantiun</p>
      <span class="btn">Read More</span>
    </div>
  </div>
</section>

<section class="gallery">
  <div class="wrap" style="height:523px">
    <h2 class="title">Image <em>Gallery</em></h2>
    <div class="filters"><span class="on">All</span><span>Events</span><span>Training</span><span>Yoga</span><span>Special</span></div>
    <div class="grid">
      <div role="img" aria-label="Portrait of the teacher outdoors" style="left:0;top:0;width:225px;height:145px;background:linear-gradient(120deg,#3b6a2a,#b09078)"></div>
      <div role="img" aria-label="Fresh fruit and vegetables" style="left:0;top:156px;width:225px;height:145px;background:linear-gradient(120deg,#b3261e,#e07a1f 45%,#3a3a7a)"></div>
      <div role="img" aria-label="Trainer coaching a client on a balance board" style="left:237px;top:0;width:224px;height:301px;background:linear-gradient(170deg,#2f4f2a,#7a6a5a 60%,#3a8fc0)"></div>
      <div role="img" aria-label="Teacher in white standing in a studio" style="left:475px;top:0;width:225px;height:145px;background:linear-gradient(120deg,#6a4a30,#c9a37a)"></div>
      <div role="img" aria-label="Black and white photo of a yoga pose" style="left:475px;top:156px;width:225px;height:145px;background:linear-gradient(120deg,#2a2a2a,#9a9a9a)"></div>
      <div role="img" aria-label="Student in a deep forward bend on a yellow mat" style="left:713px;top:0;width:223px;height:301px;background:linear-gradient(170deg,#6a5a4a,#c08050 50%,#d8a020)"></div>
    </div>
  </div>
</section>

<section class="testimonials wrap">
  <div class="text">
    <h2 class="title">Video <em>Testimonials</em></h2>
    <h5>Yes, Tom Pelling can help me with my health and wellness</h5>
    <p>Sed ut perspiciatis unde omnis iste natus error sit voluptatem accusantium doloremque laudantium, totam rloem operiam, eaque ipsainventore veritatis et quasi architecto beatae vitae dicta sunt explicab oemo enim ipsam voluptatem quia voluptassit aspernSed ut perspiciatis unde omnis iste natus error sit voluptatem accusantium doloremque laloiud antium, totam rem operiam, eaque ipsainvent.</p>
    <div class="who">Dana Hollis, City Name</div>
    <div class="role">Sed ut perspiciatis unde omnis</div>
  </div>
  <div class="video" role="img" aria-label="Video still of a smiling client in a green top">
    <svg class="play" width="56" height="56" viewBox="0 0 56 56"><circle cx="28" cy="28" r="25" fill="rgba(0,0,0,.25)" stroke="#fff" stroke-width="3"/><path d="M22 17l17 11-17 11z" fill="#fff"/></svg>
  </div>
</section>

<footer>
  <div class="site-footer">
    <div class="wrap" style="height:200px">
      <div class="foot-brand"><i></i>Tom Pelling</div>
      <div class="socials"><span></span><span></span><span></span><span></span></div>
      <div class="fcol" style="left:215px"><h6>Services</h6>Sed ut perspici<br>omnis iste natus<br>A voluptatem accusan<br>tium doloremque</div>
      <div class="fcol" style="left:385px"><h6>Trainibg</h6>Sed ut persp<br>omnis iste natus<br>A voluptate<br>ntium, totam rem</div>
      <div class="fcol" style="left:555px"><h6>How we work</h6>Sed ut perspicia<br>omnis iste natus<br>A voluptatem acc<br>tium domque</div>
      <div class="newsletter"><h6>Newsletter</h6>Lorem ipsum dolor sit amet, consectetur adipiscing elit. Nulla in purus nibh.
        <div class="subscribe"><span>Email Address:</span><b>GO</b></div>
      </div>
    </div>
  </div>
  <div class="copyright">© 2015 copyrights are reserved.tompelling.example</div>
</footer>

</body>
</html>
```